Corkly Soy Candles - New WP TEMPLATE

We make handemade soy candles in large volume and our company is now seeing huge growth, we are about to break into the retail market by providing our candles wholesale to retail outlets and gift stores.

Our candles are set apart by the fact they are very earth friendly in the sense of utilising old wine bottles that are cut in half and filling them with highly scented all natural pure soy and sealing the candle with a cork.

The website will need to be a complete Wordpress template. PLEASE ensure it is responsive and mobile friendly.

The look and feel of the website will need to be very original and rustic in feel.

Some examples of the "feel" of the site cand be found at the following links:

http://www.example-plankstudio.test/blog/2011/07/new-website-launches-for-july/

http://www.example-fernhutcabin.test/

http://www.example-glowvatlights.test/

http://www.example-sage417.test/wedding-logo/rustic-ombre-summer-wedding-website/

http://example-plumthemes.test/grunge-website-design/screen-shot-2012-02-04-at-6-22-21-pm/

Our lettering logo is simply the word "Corkly" in the font "Sweetly Broken". I have included our WORD logo and our SYMBOL logo. You will see our product in the images attached.

The site should include:

A slider
All images to be in circle cut outs (not square)

-A homepage with slider
-A section for "The Story" (This will be the largest page with a circle for each of the 6 scents and then a staggered story line of how we make the candles, alternating pictures from left to right).
-A section for "Retailers"
-A section for "Wholesale"
-A contact section

Please place some sort of placeholder images in all of the areas that will have images - were having the images done professionally and I have some design experience so I can finalise this aspect.

If you can make this a "One page template" that would be okay, but we are also open to multipage designs as long as its user friendly.

See images for the process and feel of product.

IF you think the prize needs to be increased and you have a good design that we like, we are happy to negotiate with you!

```html
<!DOCTYPE html>
<html lang="en">
<head>
<meta charset="utf-8">
<title>Corkly Soy Candles</title>
<link href="https://fonts.googleapis.com/css2?family=Oswald:wght@400;500&family=Arimo:wght@400;700&display=swap" rel="stylesheet">
<style>
:root{
  --brown:#8a4a1c;
  --brown-dark:#5e2f0e;
  --brown-light:#b8692a;
  --orange:#c9671f;
  --ink:#222;
  --muted:#555;
  --panel:#ececec;
  --panel-line:#d6d6d6;
  --night:#1d1e24;
  --night-2:#2a2b31;
  --white:#fff;
}
*{box-sizing:border-box;margin:0;padding:0}
html,body{width:1200px;height:2200px;overflow:hidden}
body{position:relative;background:var(--white);font-family:"Arimo",Arial,sans-serif;color:var(--ink)}
.abs{position:absolute}
.top-rule{left:0;top:0;width:1200px;height:3px;background:var(--brown-light)}
.nav a{position:absolute;top:58px;font-size:12px;color:var(--ink);text-decoration:none;transform:translateX(-50%);white-space:nowrap}
.brand{position:absolute;left:599px;top:22px;transform:translateX(-50%);font-family:"Oswald",sans-serif;font-weight:400;font-size:56px;color:var(--brown-dark);letter-spacing:2px;line-height:1}
.hero{left:86px;top:139px;width:1028px;height:386px;background:linear-gradient(100deg,#cfd4d3 0%,#e6e6e0 40%,#f2efe3 60%,#e4d86a 85%,#c9b938 100%)}
.bar{position:absolute;height:42px;background:linear-gradient(#9a5524,#6e3812);border-top:3px solid #b7773f;color:var(--white);font-family:"Oswald",sans-serif;font-size:22px;line-height:38px;padding-left:16px}
.products{position:absolute;left:86px;width:769px;display:flex}
.card{position:absolute;width:200px;text-align:center;transform:translateX(-50%)}
.photo{width:142px;height:142px;border-radius:50%;margin:0 auto}
.card h3{font-family:"Oswald",sans-serif;font-weight:500;font-size:19px;margin-top:20px;color:var(--ink)}
.card p{font-size:12px;color:var(--muted);line-height:19px}
.card p:first-of-type{margin-top:6px}
.btns{display:flex;gap:6px;justify-content:center;margin-top:8px}
.btn{height:22px;font-size:9px;line-height:20px;padding:0 8px;border-radius:2px}
.btn-basket{background:#eee;border:1px solid #999;color:#333}
.btn-buy{background:var(--orange);border:1px solid var(--brown-dark);color:var(--white)}
.side-head{position:absolute;left:877px;width:237px;height:42px;background:var(--night-2);color:var(--white);font-family:"Oswald",sans-serif;font-size:24px;line-height:42px;padding-left:16px;border-top:3px solid #555}
.categories{left:877px;top:592px;width:237px;height:293px;background:var(--panel);padding:6px 16px}
.categories li{list-style:none;font-size:11px;color:#777;height:43px;line-height:30px;border-bottom:1px solid var(--panel-line)}
.categories li.active{color:var(--brown)}
.news{left:877px;top:924px;width:237px;height:354px;background:var(--night);padding:8px 20px;color:var(--white)}
.news h2{font-family:"Oswald",sans-serif;font-weight:400;font-size:26px;line-height:40px}
.news .lead{color:var(--orange);font-size:12px;line-height:18px;margin-top:10px;text-transform:uppercase;padding-bottom:10px;border-bottom:1px solid #444}
.news .body{font-size:12px;line-height:19px;margin-top:16px}
.news ul{margin-top:20px}
.news li{list-style:none;font-size:10px;color:var(--orange);line-height:24px;text-transform:uppercase;padding-left:16px;position:relative}
.news li::before{content:"";position:absolute;left:0;top:9px;width:7px;height:7px;background:var(--orange)}
.story-box{left:86px;top:1342px;width:1028px;height:178px;border:1px solid #ddd;border-top:0}
.story-circle{position:absolute;top:1364px;width:136px;height:136px;border-radius:50%;transform:translateX(-50%)}
.arrows{position:absolute;left:1076px;top:1310px;display:flex;gap:4px}
.contact-title{left:110px;top:1552px;font-family:"Oswald",sans-serif;font-size:22px;color:var(--brown-dark)}
.field{position:absolute;left:110px;width:330px;border:1px solid #c8c8c8;background:#f6f6f6;font-size:10px;color:#444;padding:0 10px;line-height:39px}
.submit{position:absolute;left:110px;top:1821px;width:330px;height:39px;background:linear-gradient(#d37a2a,#8a4a1c);color:var(--white);font-weight:700;font-size:17px;text-align:center;line-height:39px;border-radius:3px}
.map{left:508px;top:1608px;width:604px;height:249px;background:linear-gradient(120deg,#cfe0ee 0%,#cfe0ee 35%,#dfe6cf 45%,#eef0e4 100%);border:1px solid #ccc}
.footer{left:0;top:1892px;width:1200px;height:308px;background:var(--night)}
.fcol{position:absolute;top:1920px;color:#aaa;font-size:12px}
.fcol h4{font-family:"Oswald",sans-serif;font-weight:400;font-size:21px;color:var(--white);margin-bottom:6px}
.fcol li{list-style:none;line-height:22px}
.fcol p{line-height:20px;width:230px}
.nl-input{position:absolute;left:838px;top:1962px;width:240px;height:44px;background:var(--white);border:3px solid #777;font-size:10px;color:#999;padding-left:14px;line-height:38px}
.nl-btn{position:absolute;left:838px;top:2023px;width:240px;height:50px;background:linear-gradient(#d37a2a,#8a4a1c);color:var(--white);font-size:13px;text-align:center;line-height:50px}
.copyright{left:0;top:2150px;width:1200px;text-align:center;color:#888;font-size:13px}
</style>
</head>
<body>
<div class="abs top-rule"></div>
<nav class="nav">
  <a style="left:115px">Home</a><a style="left:210px">About Us</a><a style="left:327px">New Products</a><a style="left:442px">Specials</a>
  <a style="left:777px">All Products</a><a style="left:887px">Reviews</a><a style="left:994px">Contact Us</a><a style="left:1090px">Faq</a>
</nav>
<div class="brand">Corkly</div>

<div class="abs hero" role="img" aria-label="Slider photo of white pillar candles with yellow orchids"></div>

<div class="bar" style="left:86px;top:550px;width:769px">Featured Products</div>
<section>
  <div class="card" style="left:176px;top:616px"><div class="photo" role="img" aria-label="Lit red candles" style="background:radial-gradient(#ffcf7a,#c2381a 60%,#3a0d05)"></div><h3>Lorem Ipsum is</h3><p>Price: $79.99</p><p>In Stock</p><p>Quantity in Basket: none</p><div class="btns"><span class="btn btn-basket">Add To Basket</span><span class="btn btn-buy">Buy Now</span></div></div>
  <div class="card" style="left:467px;top:616px"><div class="photo" role="img" aria-label="Lit candle glow" style="background:radial-gradient(#fff3c0,#d99a2e 55%,#1c1206)"></div><h3>Lorem Ipsum is</h3><p>Price: $79.99</p><p>In Stock</p><p>Quantity in Basket: none</p><div class="btns"><span class="btn btn-basket">Add To Basket</span><span class="btn btn-buy">Buy Now</span></div></div>
  <div class="card" style="left:758px;top:616px"><div class="photo" role="img" aria-label="Candle flame in the dark" style="background:radial-gradient(#ffdd88,#a8561c 50%,#140a04)"></div><h3>Lorem Ipsum is</h3><p>Price: $79.99</p><p>In Stock</p><p>Quantity in Basket: none</p><div class="btns"><span class="btn btn-basket">Add To Basket</span><span class="btn btn-buy">Buy Now</span></div></div>
</section>

<div class="side-head" style="top:550px">CATEGORIES</div>
<ul class="abs categories">
  <li class="active">Tea Light Candles</li><li>Jar Candles</li><li>Wax Melts</li><li>Pillar candles</li><li>Wax Melts</li><li>Jar Candles</li><li>Jar Candles</li>
</ul>

<div class="bar" style="left:86px;top:924px;width:769px">Wholesale</div>
<section>
  <div class="card" style="left:176px;top:988px"><div class="photo" role="img" aria-label="Glass bottle candles" style="background:radial-gradient(#dfe6d8,#7d8f70 60%,#3b4434)"></div><h3>Lorem Ipsum is</h3><p>Price: $79.99</p><p>In Stock</p><p>Quantity in Basket: none</p><div class="btns"><span class="btn btn-basket">Add To Basket</span><span class="btn btn-buy">Buy Now</span></div></div>
  <div class="card" style="left:467px;top:988px"><div class="photo" role="img" aria-label="Rows of wine bottle candles" style="background:radial-gradient(#e8e4d4,#6f7a6a 60%,#2d3330)"></div><h3>Lorem Ipsum is</h3><p>Price: $79.99</p><p>In Stock</p><p>Quantity in Basket: none</p><div class="btns"><span class="btn btn-basket">Add To Basket</span><span class="btn btn-buy">Buy Now</span></div></div>
  <div class="card" style="left:758px;top:988px"><div class="photo" role="img" aria-label="Stacked cork topped jars" style="background:radial-gradient(#e6c9a8,#a77450 60%,#6b4630)"></div><h3>Lorem Ipsum is</h3><p>Price: $79.99</p><p>In Stock</p><p>Quantity in Basket: none</p><div class="btns"><span class="btn btn-basket">Add To Basket</span><span class="btn btn-buy">Buy Now</span></div></div>
</section>

<aside class="abs news">
  <h2>LATEST NEWS</h2>
  <p class="lead">Lorem Ipsum is simply dummy text of the printing and</p>
  <p class="body">Lorem Ipsum is simply dummy text of the printing and typesetting</p>
  <ul><li>Lorem ipsum is simply</li><li>Lorem ipsum is</li><li>Lorem ipsum is simply dummy</li><li>Lorem ipsum is text</li><li>Lorem ipsum</li></ul>
</aside>

<div class="bar" style="left:86px;top:1300px;width:1028px">The Story</div>
<div class="arrows">
  <svg width="14" height="16" viewBox="0 0 14 16"><rect width="14" height="16" fill="#fff"/><path d="M10 3 L4 8 L10 13Z" fill="#5e2f0e"/></svg>
  <svg width="14" height="16" viewBox="0 0 14 16"><rect width="14" height="16" fill="#fff"/><path d="M4 3 L10 8 L4 13Z" fill="#5e2f0e"/></svg>
</div>
<div class="abs story-box"></div>
<div class="story-circle" style="left:176px;background:radial-gradient(#f4a6c8,#c2337a 55%,#1a0a10)" role="img" aria-label="Pink pillar candles"></div>
<div class="story-circle" style="left:345px;background:radial-gradient(#fbe0d0,#d42b2b 55%,#8a1010)" role="img" aria-label="Red candles"></div>
<div class="story-circle" style="left:508px;background:radial-gradient(#f6f2e4,#9fae7c 55%,#2e3a22)" role="img" aria-label="White candles with greenery"></div>
<div class="story-circle" style="left:677px;background:radial-gradient(#ffd070,#b8301a 55%,#2a0806)" role="img" aria-label="Floating tea lights"></div>
<div class="story-circle" style="left:850px;background:radial-gradient(#fbfbfb,#f1e3de 50%,#d64a3a 80%)" role="img" aria-label="Red candle in glass"></div>
<div class="story-circle" style="left:1019px;background:radial-gradient(#fbf8ee,#e4dcc4 55%,#c8b04a)" role="img" aria-label="Cream pillar candles"></div>

<h2 class="abs contact-title">CONTACT INFO</h2>
<div class="field" style="top:1608px;height:39px">Enter Your name</div>
<div class="field" style="top:1667px;height:39px">Enter Your Email</div>
<div class="field" style="top:1728px;height:71px">Message</div>
<div class="submit">SUBMIT</div>
<div class="abs map" role="img" aria-label="Map showing the shop location"></div>

<footer>
  <div class="abs footer"></div>
  <div class="fcol" style="left:86px"><h4>Navigation</h4><ul><li>Home</li><li>About</li><li>Special</li><li>New Products</li><li>Wholesale</li><li>FAQ</li><li>Contact</li></ul></div>
  <div class="fcol" style="left:230px"><h4>My Account</h4><ul><li>My Account</li><li>Forgot your password?</li><li>Cart</li></ul></div>
  <div class="fcol" style="left:403px"><h4>Our Products</h4><ul><li>Candles</li><li>Wax Candles</li></ul></div>
  <div class="fcol" style="left:574px"><h4>About us</h4><p>Lorem Ipsum is simply dummy text of the printing and typesetting industry. Lorem Ipsum has been the industry's standard dummy text ever since the 1500s, when an unknown printer took a galley of type and scrambled it to make a type specimen book.</p></div>
  <div class="fcol" style="left:838px"><h4>News letter</h4></div>
  <div class="nl-input">Enter your e-mail</div>
  <div class="nl-btn">SUBSCRIBE</div>
  <p class="abs copyright">© 2014 Candles &nbsp;/&nbsp; All Reserved</p>
</footer>
</body>
</html>
```